Personal Card: Make it roar!

Hello to all designers,
Hope you're having a nice day/evening! Let's cut to the chase. I would like a modern, beautiful and professional personal business card; with a vector-art of a lion. I'd like the lion to be Blood Red. On a black background. I'm a Filipino, and would love to have my country's flag incorporated into the design. Id like the stars of my flag to be used in your designs if possible. The texts I want on the card are only my name, number, and email address. Colour of my name should be White, and my details Silver. The size and font should be simple and professional, you're in charge of that! The placements of the lion and my details will be yours to decide.

At the back of the card, I would like just the words "Thank You" (Silver) on a Black Background. Right on the center.

To summarise, my requirements are:
- Blood Red: Front Face of Lion, Vector-Art
- Black: Background
- Yellow: Three Stars used in the design
- White: Benedict Sr Talavera
- Silver: Number & Email (Where appropriate)
- Back of the card (Center). Silver: "Thank You"
- Please DON'T use the colour blue.

It's all about the Lion. Images you'll find attached are some images of Lions' faces which I particularly want to be captured and put onto the card. Convert it into a vector-art. A vector-art Lion. PLEASE use the images attached for inspiration only! Do not use it on your designs. Thank you very much for your time.

Good luck!

Ben
Updates

Hello Desginers, Please use Blood Red for the colour red in your designs:HEX: 8A0707RGB: 138,7,7Thank you,Ben Added Saturday, March 12, 2016

Target Market(s)

Potential Connections

Industry/Entity Type

It Professional

Contact Information for Business Card

Name: Benedict Sr Talavera
Email: bentalavera@mailhaven.co.uk
Number: 07382614927

Requirements
Must have
• Modern, Professional & Simple
• (Blood Red HEX: 8A0707, RGB: 138,7,7) Lion (Vector-style art)
• (Black) Background
• (White) My Name
• (Silver) My Details
• Back of card: "Thank You" in Silver. Font size should be small/medium.
• Only colours that should be used are Red, Black, Yellow and White/Silver
Nice to have
• - Use of 3 Yellow stars on the design
Should not have
• - Please avoid using any other colours apart from those specified.

```html
<!DOCTYPE html>
<html lang="en">
<head>
<meta charset="utf-8">
<title>Benedict Sr Talavera – Business Card</title>
<link href="https://fonts.googleapis.com/css2?family=Open+Sans:wght@400;600;700&display=swap" rel="stylesheet">
<style>
  :root {
    --stage: #d9d4cc;
    --card-black: #050505;
    --card-sheen: #2a2a2a;
    --blood-red: #8a0707;
    --lion-red: #c41a1a;
    --flag-yellow: #f2e81e;
    --star-faint: #4a4410;
    --name-white: #ffffff;
    --detail-silver: #c9c9c9;
  }
  * { box-sizing: border-box; margin: 0; padding: 0; }
  html, body { width: 1200px; height: 1062px; overflow: hidden; }
  body {
    background: var(--stage);
    font-family: "Open Sans", Arial, sans-serif;
    position: relative;
  }
  .card {
    position: absolute;
    left: 180px;
    width: 840px;
    height: 480px;
    overflow: hidden;
    background: radial-gradient(ellipse at 45% 55%, var(--card-sheen) 0%, var(--card-black) 60%);
    box-shadow: 0 10px 30px rgba(0,0,0,0.35);
  }
  .card--front { top: 34px; }
  .card--back { top: 548px; }

  .card__art { position: absolute; inset: 0; width: 100%; height: 100%; }

  .lion-art {
    position: absolute;
    border-radius: 50% 46% 48% 52%;
    background: radial-gradient(circle at 55% 45%, #1a0000 0%, #1a0000 22%, var(--lion-red) 24%, var(--blood-red) 100%);
  }
  .card--front .lion-art { left: 170px; top: 70px; width: 260px; height: 200px; }
  .card--back .lion-art { left: 300px; top: 150px; width: 310px; height: 230px; }

  .contact {
    position: absolute;
    left: 470px;
    top: 112px;
    list-style: none;
    color: var(--detail-silver);
    font-size: 19px;
    line-height: 34px;
  }
  .contact__item { display: flex; align-items: center; gap: 12px; }
  .contact__icon { width: 16px; height: 16px; flex: none; }

  .identity {
    position: absolute;
    left: 60px;
    top: 345px;
  }
  .identity__name {
    color: var(--name-white);
    font-weight: 700;
    font-size: 34px;
    line-height: 1.1;
  }
  .identity__role {
    color: var(--detail-silver);
    font-size: 20px;
    margin-top: 2px;
  }

  .thanks {
    position: absolute;
    left: 60px;
    top: 240px;
    transform: translate(-50%, -50%) rotate(90deg);
    transform-origin: center;
    color: var(--detail-silver);
    font-weight: 700;
    font-size: 28px;
    white-space: nowrap;
  }
</style>
</head>
<body>

<section class="card card--front" aria-label="Business card front">
  <svg class="card__art" viewBox="0 0 840 480" aria-hidden="true">
    <polygon class="star star--faint" fill="var(--star-faint)" opacity="0.8"
      points="300,30 312,66 350,66 319,88 331,124 300,102 269,124 281,88 250,66 288,66"/>
    <polygon class="star star--faint" fill="var(--star-faint)" opacity="0.8"
      points="150,150 160,180 192,180 166,198 176,228 150,210 124,228 134,198 108,180 140,180"/>
    <path class="swoosh swoosh--red" fill="var(--blood-red)"
      d="M300 480 C 520 420, 700 330, 840 215 L840 480 Z"/>
    <path class="swoosh swoosh--yellow" fill="none" stroke="var(--flag-yellow)" stroke-width="14"
      d="M250 480 C 480 410, 680 320, 840 200"/>
    <line x1="405" y1="220" x2="455" y2="248" stroke="var(--lion-red)" stroke-width="2"/>
  </svg>

  <div class="lion-art" role="img" aria-label="Blood red vector-art lion head with flowing mane"></div>

  <ul class="contact">
    <li class="contact__item">
      <svg class="contact__icon" viewBox="0 0 16 16" aria-hidden="true"><path fill="var(--detail-silver)" d="M4 1 L6 4 L5 6 C6 8 8 10 10 11 L12 10 L15 12 L13 15 C7 15 1 9 1 3 Z"/></svg>
      <span>07382614927</span>
    </li>
    <li class="contact__item">
      <svg class="contact__icon" viewBox="0 0 16 16" aria-hidden="true"><g fill="none" stroke="var(--detail-silver)" stroke-width="1.3"><circle cx="8" cy="8" r="6.5"/><ellipse cx="8" cy="8" rx="3" ry="6.5"/><line x1="1.5" y1="8" x2="14.5" y2="8"/></g></svg>
      <span>www.harlowfield.com</span>
    </li>
    <li class="contact__item">
      <svg class="contact__icon" viewBox="0 0 16 16" aria-hidden="true"><text x="8" y="13" text-anchor="middle" font-size="15" font-weight="700" fill="var(--detail-silver)" font-family="Open Sans, sans-serif">@</text></svg>
      <span>bentalavera@mailhaven.co.uk</span>
    </li>
  </ul>

  <div class="identity">
    <h1 class="identity__name">Benedict Sr Talavera</h1>
    <p class="identity__role">Manager</p>
  </div>
</section>

<section class="card card--back" aria-label="Business card back">
  <svg class="card__art" viewBox="0 0 840 480" aria-hidden="true">
    <polygon class="star" fill="var(--flag-yellow)"
      points="440,20 462,86 532,86 476,127 497,193 440,152 383,193 404,127 348,86 418,86"/>
    <polygon class="star" fill="var(--flag-yellow)"
      points="260,190 278,244 335,244 289,277 307,331 260,298 213,331 231,277 185,244 242,244"/>
    <polygon class="star" fill="var(--flag-yellow)"
      points="650,300 670,360 734,360 682,397 702,457 650,420 598,457 618,397 566,360 630,360"/>
  </svg>

  <div class="lion-art" role="img" aria-label="Blood red vector-art lion head with flowing mane"></div>

  <p class="thanks">Thank You</p>
</section>

</body>
</html>
```